brake hoses

revamp current brake hose flyer - modernize make it look better

please use website
Kestrelmotorworks.co.nz for as much as possible

i want you all to come with own wording description etc

```html
<!DOCTYPE html>
<html lang="en">
<head>
<meta charset="utf-8">
<title>Kestrel Motorworks – Brake Hoses and Pipes Flyer</title>
<link rel="stylesheet" href="https://fonts.googleapis.com/css2?family=Poppins:wght@400;500;600;700;800&display=swap">
<style>
  :root {
    --yellow: #fdd800;
    --yellow-deep: #e8c400;
    --charcoal: #3c3c3c;
    --charcoal-dark: #2b2b2b;
    --ink: #111111;
    --white: #ffffff;
    --page: #f4f4f4;
    --aim-red: #e5254e;
  }
  * { box-sizing: border-box; margin: 0; padding: 0; }
  html, body {
    width: 1200px; height: 2425px; overflow: hidden;
    background: var(--page);
    font-family: "Poppins", sans-serif;
  }
  .canvas { position: relative; width: 1200px; height: 2425px; }
  .flyer {
    position: absolute; left: 0; top: 436px;
    width: 1000px; height: 1293px;
    transform: scale(1.2); transform-origin: 0 0;
    background: var(--white); overflow: hidden;
  }
  .abs { position: absolute; white-space: nowrap; }

  /* hero */
  .hero-photo {
    left: 0; top: 0; width: 1000px; height: 530px;
    background: linear-gradient(115deg, #555 0%, #3a3a3a 45%, #2f2f2f 100%);
  }
  .hero-shapes { left: 0; top: 0; width: 1000px; height: 530px; }
  .brake-photo {
    left: 520px; top: 100px; width: 400px; height: 370px;
    border-radius: 50%;
    background: radial-gradient(circle at 45% 45%, #d6d6d6 0%, #9a9a9a 45%, #5a5a5a 75%, rgba(90,90,90,0) 100%);
  }
  .brand-name {
    left: 0; width: 510px; top: 190px; text-align: center;
    color: var(--yellow); font-weight: 800; font-size: 64px; letter-spacing: 4px;
  }
  .brand-sub {
    left: 0; width: 510px; top: 276px; text-align: center;
    color: var(--white); font-weight: 500; font-size: 25px; letter-spacing: 1px;
  }
  .headline {
    left: 56px; top: 312px; font-weight: 800; font-size: 58px; line-height: 56px;
  }
  .headline .line-1 { color: var(--yellow); display: block; }
  .headline .line-2 { color: var(--white); display: block; }
  .range-band {
    left: 56px; top: 455px; color: var(--ink); font-weight: 700; font-size: 25px;
  }

  /* product grid */
  .product-tile {
    width: 186px; height: 112px; border: 4px solid var(--yellow);
    background: linear-gradient(160deg, #4a4a4a, #2e2e2e);
  }

  /* aim */
  .aim-title {
    left: 108px; top: 962px; font-weight: 700; font-size: 40px; color: var(--ink);
  }
  .aim-icon { left: 55px; top: 966px; }
  .aim-text {
    left: 55px; top: 1012px; width: 360px; font-size: 22px; line-height: 27px; color: var(--ink);
    white-space: normal;
  }

  /* footer */
  .footer-shapes { left: 0; top: 1110px; width: 1000px; height: 183px; }
  .phones { left: 55px; top: 1132px; color: var(--white); font-weight: 700; font-size: 30px; line-height: 41px; }
  .phones .row { display: flex; align-items: center; gap: 12px; }
  .unsub { left: 55px; top: 1217px; color: var(--yellow); font-size: 16px; letter-spacing: 1.5px; }
  .contact-strip {
    left: 378px; top: 1140px; width: 610px; display: flex; gap: 30px;
    color: var(--white); font-size: 16px; align-items: center;
  }
  .contact-strip span { display: flex; align-items: center; gap: 10px; }
  .address-line {
    left: 396px; top: 1203px; display: flex; align-items: center; gap: 14px;
    color: var(--charcoal); font-weight: 600; font-size: 19px;
  }
  .address-line .company { font-size: 22px; font-weight: 600; }

  /* right column */
  .centre-title {
    left: 490px; width: 470px; top: 540px; text-align: center;
    font-weight: 800; font-size: 36px; line-height: 44px; color: var(--ink);
  }
  .specialise-box {
    left: 512px; top: 644px; width: 428px; height: 126px;
    border: 2px dashed var(--charcoal);
  }
  .specialise-title {
    left: 560px; width: 332px; top: 618px; text-align: center; background: var(--white);
    font-weight: 700; font-size: 25px; line-height: 26px; color: var(--charcoal);
    white-space: normal;
  }
  .spec-item { display: flex; align-items: center; gap: 14px; font-weight: 700; font-size: 21px; color: var(--charcoal); line-height: 26px; }
  .yellow-dot {
    width: 62px; height: 62px; border-radius: 50%; background: var(--yellow);
    border: 2px solid var(--ink); display: flex; align-items: center; justify-content: center;
  }
  .service-tile {
    background: var(--charcoal); color: var(--white); font-size: 17px; line-height: 23px;
    text-align: center; display: flex; align-items: center; justify-content: center;
  }
  .service-icon {
    width: 44px; height: 44px; border-radius: 50%; background: var(--yellow);
    border: 2px solid var(--charcoal); display: flex; align-items: center; justify-content: center;
  }
  .freephone { left: 503px; top: 1068px; height: 54px; display: flex; font-weight: 700; font-size: 27px; }
  .freephone .label { background: var(--yellow); color: var(--ink); width: 190px; display: flex; align-items: center; justify-content: center; }
  .freephone .number { background: var(--charcoal); color: var(--white); width: 250px; display: flex; align-items: center; justify-content: center; letter-spacing: 0.5px; }
</style>
</head>
<body>
<div class="canvas">
  <div class="flyer">

    <!-- hero -->
    <div class="abs hero-photo" role="img" aria-label="Greyscale photo of a mechanic working on a car wheel"></div>
    <svg class="abs hero-shapes" viewBox="0 0 1000 530" aria-hidden="true">
      <defs>
        <linearGradient id="triFill" x1="0" y1="0" x2="0" y2="1">
          <stop offset="0" stop-color="#f5d400"/>
          <stop offset="1" stop-color="#d9b800"/>
        </linearGradient>
      </defs>
      <polygon points="725,0 1000,0 1000,530 405,530" fill="url(#triFill)"/>
      <polygon points="0,445 420,445 385,500 0,500" fill="#fdd800"/>
      <polygon points="0,500 385,500 410,530 0,530" fill="#ffffff"/>
    </svg>
    <div class="abs brake-photo" role="img" aria-label="Photo of a brake disc and caliper assembly"></div>

    <div class="abs brand-name">KESTREL</div>
    <div class="abs brand-sub">KESTREL MOTORWORKS</div>
    <div class="abs headline"><span class="line-1">BRAKE HOSES</span><span class="line-2">AND PIPES</span></div>
    <div class="abs range-band">LARGE RANGE OF HOSES</div>

    <!-- product photos -->
    <div class="abs product-tile" style="left:57px;top:550px" role="img" aria-label="Photo of braided brake hoses with banjo fittings"></div>
    <div class="abs product-tile" style="left:274px;top:550px" role="img" aria-label="Photo of a bent metal brake pipe"></div>
    <div class="abs product-tile" style="left:57px;top:682px" role="img" aria-label="Photo of hose retaining clips and brackets"></div>
    <div class="abs product-tile" style="left:276px;top:682px" role="img" aria-label="Photo of brass pipe nuts"></div>
    <div class="abs product-tile" style="left:59px;top:815px" role="img" aria-label="Photo of black rubber brake hoses"></div>
    <div class="abs product-tile" style="left:276px;top:815px" role="img" aria-label="Photo of a row of brass fittings"></div>

    <!-- aim -->
    <svg class="abs aim-icon" width="42" height="42" viewBox="0 0 42 42" aria-hidden="true">
      <circle cx="20" cy="22" r="18" fill="var(--aim-red)"/>
      <circle cx="20" cy="22" r="11" fill="#fff"/>
      <circle cx="20" cy="22" r="5" fill="var(--aim-red)"/>
      <path d="M20 22 L36 6" stroke="#3a6fd8" stroke-width="3"/>
      <path d="M32 4 L38 4 L38 10" stroke="#3a6fd8" stroke-width="3" fill="none"/>
    </svg>
    <div class="abs aim-title">OUR AIM</div>
    <div class="abs aim-text">is to have your parts repaired with the quickest turn-around times possible</div>

    <!-- right column -->
    <div class="abs centre-title">KESTREL MOTORWORKS</div>
    <div class="abs specialise-box"></div>
    <div class="abs specialise-title">SPECIALISE IN THE MANUFACTURE OF</div>
    <div class="abs spec-item" style="left:535px;top:686px">
      <div class="yellow-dot">
        <svg width="40" height="30" viewBox="0 0 40 30" aria-hidden="true"><ellipse cx="20" cy="15" rx="17" ry="11" fill="none" stroke="#111" stroke-width="5"/></svg>
      </div>RUBBER
    </div>
    <div class="abs spec-item" style="left:740px;top:686px">
      <div class="yellow-dot">
        <svg width="34" height="40" viewBox="0 0 34 40" aria-hidden="true"><path d="M9 4 V30" stroke="#111" stroke-width="5"/><circle cx="18" cy="26" r="9" fill="none" stroke="#111" stroke-width="5"/><circle cx="18" cy="26" r="3" fill="#111"/></svg>
      </div><span>BRAIDED<br>HOSES</span>
    </div>

    <!-- services row 1 -->
    <div class="abs service-tile" style="left:494px;top:830px;width:97px;height:66px;padding-top:14px">Oil</div>
    <div class="abs service-tile" style="left:611px;top:830px;width:97px;height:66px;padding-top:14px">Fuel</div>
    <div class="abs service-tile" style="left:729px;top:830px;width:97px;height:66px;padding-top:14px">Brake</div>
    <div class="abs service-tile" style="left:839px;top:830px;width:97px;height:66px;padding-top:14px">Braided</div>
    <div class="abs service-icon" style="left:520px;top:807px"><svg width="22" height="22" viewBox="0 0 22 22" aria-hidden="true"><path d="M11 2 C11 2 4 11 4 14 a7 7 0 0 0 14 0 C18 11 11 2 11 2Z" fill="#111"/></svg></div>
    <div class="abs service-icon" style="left:637px;top:807px"><svg width="22" height="22" viewBox="0 0 22 22" aria-hidden="true"><rect x="4" y="6" width="10" height="14" fill="#111"/><path d="M14 8 L19 12 V18" stroke="#111" stroke-width="2" fill="none"/></svg></div>
    <div class="abs service-icon" style="left:755px;top:807px"><svg width="22" height="22" viewBox="0 0 22 22" aria-hidden="true"><circle cx="11" cy="11" r="8" fill="none" stroke="#111" stroke-width="2.5"/><circle cx="11" cy="11" r="3" fill="#111"/></svg></div>
    <div class="abs service-icon" style="left:865px;top:807px"><svg width="22" height="22" viewBox="0 0 22 22" aria-hidden="true"><path d="M3 18 V11 a8 8 0 0 1 16 0 V18 Z" fill="none" stroke="#111" stroke-width="2.5"/><circle cx="11" cy="12" r="2.5" fill="#111"/></svg></div>

    <!-- services row 2 -->
    <div class="abs service-tile" style="left:497px;top:937px;width:133px;height:93px;padding-bottom:20px">Powersteering</div>
    <div class="abs service-tile" style="left:643px;top:937px;width:140px;height:93px">Air<br>conditioning</div>
    <div class="abs service-tile" style="left:798px;top:937px;width:140px;height:93px">Brake &amp; fuel<br>pipes &amp; fittings</div>
    <div class="abs service-icon" style="left:541px;top:914px"><svg width="24" height="24" viewBox="0 0 24 24" aria-hidden="true"><circle cx="12" cy="12" r="9" fill="none" stroke="#111" stroke-width="2.5"/><circle cx="12" cy="12" r="3" fill="#111"/><path d="M12 3 V9 M3 12 H9 M21 12 H15" stroke="#111" stroke-width="2"/></svg></div>
    <div class="abs service-icon" style="left:691px;top:914px"><svg width="24" height="24" viewBox="0 0 24 24" aria-hidden="true"><rect x="3" y="5" width="18" height="7" fill="none" stroke="#111" stroke-width="2"/><path d="M7 14 V20 M11 14 V20 M15 14 V20 M19 14 V20" stroke="#111" stroke-width="1.6"/></svg></div>
    <div class="abs service-icon" style="left:846px;top:914px"><svg width="24" height="24" viewBox="0 0 24 24" aria-hidden="true"><rect x="3" y="12" width="18" height="6" rx="2" fill="#111"/><path d="M6 12 L9 7 H15 L18 12" fill="#111"/><path d="M8 4 V7 M16 4 V7" stroke="#111" stroke-width="2"/></svg></div>

    <div class="abs freephone"><div class="label">FREE PHONE</div><div class="number">0800 55 27 39</div></div>

    <!-- footer -->
    <svg class="abs footer-shapes" viewBox="0 0 1000 183" aria-hidden="true">
      <polygon points="343,25 1000,25 1000,70 360,70" fill="var(--charcoal)"/>
      <polygon points="360,70 1000,70 1000,183 400,183" fill="var(--yellow)"/>
      <polygon points="0,0 320,0 388,183 0,183" fill="var(--charcoal)"/>
    </svg>

    <div class="abs phones">
      <div class="row"><svg width="26" height="26" viewBox="0 0 24 24" aria-hidden="true"><path d="M6 3 L9 3 L10.5 8 L8.5 9.5 a11 11 0 0 0 6 6 L16 13.5 L21 15 V18 a2 2 0 0 1 -2 2 A16 16 0 0 1 4 5 a2 2 0 0 1 2 -2Z" fill="var(--yellow)"/></svg>07 555 0179</div>
      <div class="row"><svg width="26" height="26" viewBox="0 0 24 24" aria-hidden="true"><rect x="6" y="3" width="12" height="6" fill="var(--yellow)"/><rect x="2" y="9" width="20" height="9" rx="2" fill="var(--yellow)"/><rect x="6" y="14" width="12" height="7" fill="var(--charcoal)" stroke="var(--yellow)" stroke-width="2"/></svg>07 555 0178</div>
    </div>
    <div class="abs unsub">Unsubscribe from this list</div>

    <div class="abs contact-strip">
      <span><svg width="20" height="18" viewBox="0 0 20 18" aria-hidden="true"><rect x="1" y="3" width="18" height="13" fill="var(--yellow)"/><path d="M1 3 L10 10 L19 3" stroke="#3c3c3c" stroke-width="1.6" fill="none"/></svg>parts@kestrelmotorworks.co.nz</span>
      <span><svg width="20" height="20" viewBox="0 0 20 20" aria-hidden="true"><circle cx="10" cy="10" r="8.5" fill="none" stroke="var(--yellow)" stroke-width="2"/><ellipse cx="10" cy="10" rx="3.5" ry="8.5" fill="none" stroke="var(--yellow)" stroke-width="1.6"/><path d="M1.5 10 H18.5" stroke="var(--yellow)" stroke-width="1.6"/></svg>www.kestrelmotorworks.co.nz</span>
    </div>

    <div class="abs address-line">
      <span class="company">KESTREL MOTORWORKS</span>
      <svg width="16" height="20" viewBox="0 0 16 20" aria-hidden="true"><path d="M8 1 a6 6 0 0 1 6 6 c0 5 -6 12 -6 12 s-6 -7 -6 -12 a6 6 0 0 1 6 -6Z" fill="none" stroke="#3c3c3c" stroke-width="2"/><circle cx="8" cy="7" r="2" fill="#3c3c3c"/></svg>
      <span>12 Tamar Street, Ridgefield</span>
    </div>

  </div>
</div>
</body>
</html>
```